Tito - Lumora Estudos

2x Design Concepts for the home page and interior pages based on the attached brief and powerpoint presentation.

Colours: see 2.1 logo and heading for logo colours and website colours

Home Page: (please see attached file)
1)Logo to appear in the top left, heading to include telephone numbers and a best price (credibility stamp) - see 2.1
2)the toolbar is to be centered at the top. Emphasis must be placed on the 5 easy steps to study english in Australia - see 2.2
3) modules. 5x modules required in the home page for: home page image rotator, online quote tool, enquiry form, best deals, quick links (there are 2 examples for the quick links module - open to suggestions) - see 2.3
4) footer. the footer is to include partner logos with hyperlinks to the partner websites. with a copywright section at the base - see 2.4
5) 2.5 is the basic idea - open to design suggestions. The website objective is to submit an online quote or contact Lumora Estudos.

Internal Page: - see 3-
open to all suggestion. Require a lot of space for internal custom design concepts (these are taking place inhouse). The interior page must have a side module toolbar to include:
1) a modified online quote tool
2) modified enquiry form
3) modified quick links section

Target Market(s)

target market is young (17-30yrs) Brazilians looking to study English in Australia or continue studying English in Australia that can also acquire visa sponsorship.

The buyer will be the parents of the students. the design must appeal to both markets.

Number of Pages Required

2 pages

Requirements
Must have
• see project overview
2x design concepts for the home page and interior page
professional, clean, simple and easy to navigate

```html
<!DOCTYPE html>
<html lang="pt-BR">
<head>
<meta charset="utf-8">
<title>Lumora Estudos – Home</title>
<link href="https://fonts.googleapis.com/css2?family=Arimo:ital,wght@0,400;0,700;1,700&family=Open+Sans:wght@400;600;700&display=swap" rel="stylesheet">
<style>
:root{
  --backdrop:#03532f;
  --page:#ffffff;
  --navy:#2a5793;
  --navy-dark:#1f4778;
  --orange:#e8731f;
  --deal:#e0601a;
  --brand-green:#0c5a3a;
  --title-green:#1f8a5c;
  --text:#555;
  --muted:#888;
  --panel:#ebe8ec;
  --footer:#f3f6fa;
  --footer-link:#3a5fa0;
  --gold:#c9962a;
}
*{box-sizing:border-box;margin:0;padding:0}
html,body{width:892px;height:1200px;overflow:hidden}
body{background:var(--backdrop);font-family:"Arimo",Arial,sans-serif;position:relative}
.abs{position:absolute}
.page{position:absolute;left:62px;top:57px;width:768px;height:1085px;background:var(--page)}

/* header */
.brand{left:133px;top:108px;font:700 21px "Arimo",sans-serif;color:var(--brand-green);letter-spacing:.3px}
.stamp{left:555px;top:90px;width:66px;height:66px;border-radius:50%;background:radial-gradient(circle,#e0b54a,var(--gold));border:2px solid #b07f1c}
.flag{width:24px;height:17px;left:627px}
.flag-au{top:104px;background:#1f3c8f}
.flag-br{top:125px;background:#1f9a3c}
.phone{left:661px;font:400 13.5px "Arimo",sans-serif;color:#111}

/* navigation */
.nav-bar{left:164px;top:180px;width:563px;height:26px;border-radius:13px;background:var(--navy)}
.nav-steps{left:300px;top:173px;width:338px;height:41px;background:var(--orange);border-radius:3px}
.nav-item{color:#fff;font:400 12.5px "Arimo",sans-serif;top:186px;white-space:nowrap}
.nav-item.two{top:181px;line-height:12px;text-align:center;font-size:11.5px}
.step{top:187px;width:11px;height:11px;border-radius:50%;background:#fff;color:var(--navy);font:700 8px/11px "Arimo",sans-serif;text-align:center}
.dropdown{left:312px;top:208px;width:128px}
.dropdown li{list-style:none;height:15.5px;line-height:15.5px;text-align:center;color:#fff;font-size:12px;border-bottom:1px solid #fff}
.dropdown li:nth-child(odd){background:var(--navy-dark)}
.dropdown li:nth-child(even){background:var(--orange)}

/* hero */
.hero{left:85px;top:223px;width:406px;height:228px;border-radius:24px 24px 24px 24px;background:linear-gradient(135deg,#e0802f 0%,#c9a486 35%,#6f8fb0 65%,#2a4f86 100%);border:1px solid #ccc}

/* quote */
.quote{left:500px;top:226px;width:292px;height:223px;border:1px solid #e2e2e2}
.quote h2{position:absolute;left:8px;top:11px;font:600 15px "Open Sans",sans-serif;color:var(--title-green)}
.label{font:400 13px "Open Sans",sans-serif;color:#555}
.radio{left:521px;font:400 11.5px "Open Sans",sans-serif;color:#444}
.radio::before{content:"";display:inline-block;width:8px;height:8px;border:1.5px solid #555;border-radius:50%;margin-right:6px;vertical-align:-1px;background:radial-gradient(circle,#333 35%,transparent 40%)}
.select{left:619px;top:296px;width:151px;height:17px;border:1px solid #777;font:400 11px/15px "Open Sans",sans-serif;color:#333;padding-left:6px}
.select::after{content:"";position:absolute;right:1px;top:1px;width:13px;height:13px;background:#ddd}
.btn{left:630px;top:335px;width:65px;height:18px;border-radius:4px;background:var(--orange);color:#fff;font:700 9px/18px "Arimo",sans-serif;text-align:center}
.card{top:380px;width:27px;height:19px;border-radius:2px}

/* deals */
.deals-box{left:88px;top:460px;width:331px;height:272px;border:1px solid #e0e0e0}
.deals{left:96px;top:469px;width:314px;height:259px;background:var(--panel)}
.deals h3{position:absolute;left:18px;top:8px;font:italic 700 18px "Arimo",sans-serif;color:#7a7a7a}
.row{left:111px;width:289px;height:37.5px;font:700 14px/37.5px "Arimo",sans-serif;color:var(--deal)}
.row.light{background:#fff}
.row .city{position:absolute;left:8px}
.row .price{position:absolute;right:6px;color:#8a8a8a}
.more-flights{left:115px;top:693px;font:700 14px "Arimo",sans-serif;color:#888;text-decoration:underline}

/* contact */
.contact{left:88px;top:737px;width:331px;height:193px;border:1px solid #e0e0e0}
.contact h3{position:absolute;left:16px;top:6px;font:600 16.5px "Open Sans",sans-serif;color:var(--title-green)}
.contact p{position:absolute;left:16px;top:30px;width:282px;font:400 10.5px/14px "Open Sans",sans-serif;color:#444;text-align:justify}
.field{left:105px;width:270px;height:21px;border:1px solid #f3e8f3;background:linear-gradient(#fff,#fbf3fb);font:400 10px/19px "Open Sans",sans-serif;color:#999;padding-left:6px}

/* quick links */
.links{left:424px;top:460px;width:370px;height:470px;border:1px solid #e0e0e0}
.link-bg{left:471px;width:275px;background:#fafafa}
.thumb{left:477px;width:61px;height:60px;border-radius:5px}
.link-title{left:544px;font:600 12.5px "Open Sans",sans-serif;color:#555}
.link-text{left:542px;width:205px;font:400 10.5px/14px "Open Sans",sans-serif;color:#666}
.link-more{left:700px;width:38px;text-align:right;font:600 12.5px "Open Sans",sans-serif;color:var(--orange)}

/* footer */
.top-tab{left:195px;top:936px;width:51px;height:16px;border-radius:6px 6px 0 0;background:var(--footer);font:400 7.5px/16px "Open Sans",sans-serif;color:#6a86b6;text-align:center}
.footer{left:81px;top:952px;width:729px;height:165px;background:var(--footer)}
.f-head{font:700 7.5px "Open Sans",sans-serif;color:var(--footer-link)}
.f-link{font:400 7.5px "Open Sans",sans-serif;color:#555}
.partner{font:700 14px "Arimo",sans-serif;color:var(--footer-link)}
.f-rule{left:105px;top:1070px;width:705px;height:1px;background:#dde3ea}
.legal{left:186px;top:1087px;width:600px;font:400 6.8px/9.5px "Open Sans",sans-serif;color:#5a7fbf}
.legal strong{font-weight:700;color:var(--footer-link)}
</style>
</head>
<body>
<div class="page"></div>

<!-- header -->
<div class="abs brand">LUMORA ESTUDOS</div>
<div class="abs stamp" role="img" aria-label="Selo de melhor preço"></div>
<div class="abs flag flag-au" role="img" aria-label="Bandeira da Austrália"></div>
<div class="abs flag flag-br" role="img" aria-label="Bandeira do Brasil"></div>
<div class="abs phone" style="top:106px">0 800 555 0101</div>
<div class="abs phone" style="top:124px">1 800 555 0102</div>

<!-- navigation -->
<div class="abs nav-bar"></div>
<div class="abs nav-steps"></div>
<div class="abs nav-item" style="left:183px">Home</div>
<div class="abs nav-item" style="left:237px">Promocoes</div>
<div class="abs step" style="left:307px">1</div>
<div class="abs nav-item" style="left:324px">Cidades</div>
<div class="abs step" style="left:375px">2</div>
<div class="abs nav-item" style="left:392px">Escolas</div>
<div class="abs step" style="left:439px">3</div>
<div class="abs nav-item two" style="left:456px">Passagem<br>Aerea</div>
<div class="abs step" style="left:516px">4</div>
<div class="abs nav-item" style="left:530px">Visto</div>
<div class="abs step" style="left:562px">5</div>
<div class="abs nav-item" style="left:577px">Embarque</div>
<div class="abs nav-item" style="left:644px">Contato</div>
<div class="abs nav-item" style="left:695px">Blog</div>

<!-- hero -->
<div class="abs hero" role="img" aria-label="Foto de grupo de jovens estudantes sorrindo e fazendo sinal de positivo"></div>
<ul class="abs dropdown">
  <li>Sydney</li><li>Melbourne</li><li>Gold Coast</li><li>Brisbane</li><li>Perth</li><li>Adelaide</li><li>Others</li>
</ul>

<!-- quote -->
<div class="abs quote"><h2>→ COTAÇÃO ON-LINE</h2></div>
<div class="abs label" style="left:519px;top:273px">CIDADE</div>
<div class="abs label" style="left:617px;top:274px">DURAÇÃO</div>
<div class="abs radio" style="top:295px">Sydney</div>
<div class="abs radio" style="top:316px">Melbourne</div>
<div class="abs radio" style="top:337px">Gold Coast</div>
<div class="abs radio" style="top:358px">Brisbane</div>
<div class="abs radio" style="top:379px">Perth</div>
<div class="abs radio" style="top:400px">Adelaide</div>
<div class="abs radio" style="top:421px">Byron Bay</div>
<div class="abs select">2 Semanas</div>
<div class="abs btn">PROCURAR</div>
<div class="abs card" style="left:627px;background:#2b4a9a"></div>
<div class="abs card" style="left:671px;background:#e6453a;border-radius:50%;width:30px"></div>
<div class="abs card" style="left:717px;background:#3c8fd0"></div>
<div class="abs card" style="left:752px;background:#c9d3e3"></div>

<!-- deals -->
<div class="abs deals-box"></div>
<div class="abs deals"><h3>IN AUSTRALIA</h3></div>
<div class="abs row" style="top:504px"><span class="city">Brisbane</span><span class="price">from $89*</span></div>
<div class="abs row light" style="top:542px"><span class="city">Ballina Byron Bay</span><span class="price">from $79*</span></div>
<div class="abs row" style="top:579px"><span class="city">Gold Coast</span><span class="price">from $75*</span></div>
<div class="abs row light" style="top:617px"><span class="city">Hamilton Island</span><span class="price">from $159*</span></div>
<div class="abs row" style="top:654px"><span class="city">Launceston</span><span class="price">from $89*</span></div>
<div class="abs more-flights">More Domestic Flights</div>

<!-- contact -->
<div class="abs contact">
  <h3>ENTRE EM CONTATO</h3>
  <p>Lorem ipsum dolor sit amet, consectetuer adipiscing elit, sed diam nonummy nibh euismod tincidunt.</p>
</div>
<div class="abs field" style="top:804px">Nome:</div>
<div class="abs field" style="top:830px">E-mail:</div>
<div class="abs field" style="top:856px">Telefone:</div>
<div class="abs field" style="top:882px">Mensagem:</div>

<!-- quick links -->
<div class="abs links"></div>

<div class="abs link-bg" style="top:472px;height:78px"></div>
<div class="abs thumb" style="top:485px;background:linear-gradient(135deg,#7ccf6a,#2e9a3e)" role="img" aria-label="Mapa de rotas de voo"></div>
<div class="abs link-title" style="top:482px">Where we fly</div>
<div class="abs link-text" style="top:502px">International and Domestic route maps</div>
<div class="abs link-more" style="top:531px">More</div>

<div class="abs link-bg" style="top:558px;height:86px"></div>
<div class="abs thumb" style="top:565px;background:linear-gradient(135deg,#f04a3a,#b80f12)" role="img" aria-label="Carro vermelho de aluguel"></div>
<div class="abs link-title" style="top:561px;left:541px">Cars</div>
<div class="abs link-text" style="top:582px">Discounted car rental rates from Rodavia and Carlo. Plus earn Aerolis Frequent Flyer points</div>
<div class="abs link-more" style="top:624px;left:697px">More</div>

<div class="abs link-bg" style="top:650px;height:70px"></div>
<div class="abs thumb" style="top:655px;background:linear-gradient(135deg,#f0b86a,#b8783a)" role="img" aria-label="Criança sorrindo"></div>
<div class="abs link-title" style="top:651px">BrightKids</div>
<div class="abs link-text" style="top:672px">Help improve the lives of some of the world's poorest children</div>
<div class="abs link-more" style="top:700px;left:698px">More</div>

<div class="abs link-bg" style="top:738px;height:84px"></div>
<div class="abs thumb" style="top:743px;background:linear-gradient(#8ec0ea,#3d7cc0)" role="img" aria-label="Pessoa saltando no céu azul"></div>
<div class="abs link-title" style="top:739px;left:546px">Activities</div>
<div class="abs link-text" style="top:760px;left:546px">Endless Summer Pass for Gold Coast Theme Parks and other great activities...</div>
<div class="abs link-more" style="top:802px;left:701px">More</div>

<div class="abs thumb" style="top:834px;background:linear-gradient(135deg,#f04a3a,#b80f12)" role="img" aria-label="Carro vermelho de aluguel"></div>
<div class="abs link-title" style="top:831px;left:541px">Cars</div>
<div class="abs link-text" style="top:852px">Discounted car rental rates from Rodavia and Carlo. Plus earn Aerolis Frequent Flyer points</div>
<div class="abs link-more" style="top:894px;left:697px">More</div>

<!-- footer -->
<div class="abs top-tab">▴ Topo</div>
<div class="abs footer"></div>

<div class="abs f-head" style="left:184px;top:976px">Pagora</div>
<div class="abs f-link" style="left:184px;top:991px">Quem somos</div>
<div class="abs f-link" style="left:184px;top:1007px">Parceiros</div>
<div class="abs f-link" style="left:184px;top:1022px">Na mídia</div>
<div class="abs f-link" style="left:184px;top:1038px">Mapa do site</div>

<div class="abs f-head" style="left:281px;top:976px">Serviços</div>
<div class="abs f-link" style="left:281px;top:991px">Para vendedores</div>
<div class="abs f-link" style="left:281px;top:1007px">Para compradores</div>
<div class="abs f-link" style="left:281px;top:1022px">Tarifas</div>

<div class="abs f-head" style="left:399px;top:976px">Usuário</div>
<div class="abs f-link" style="left:399px;top:991px">Login</div>
<div class="abs f-link" style="left:399px;top:1007px">Cadastro</div>
<div class="abs f-link" style="left:399px;top:1022px">Termos de uso</div>
<div class="abs f-link" style="left:399px;top:1038px">Segurança para vendedores</div>
<div class="abs f-link" style="left:399px;top:1054px">Segurança para compradores</div>

<div class="abs f-link" style="left:590px;top:973px">Empresa do portfólio</div>
<div class="abs f-link" style="left:719px;top:990px">Parceiros</div>
<div class="abs" style="left:590px;top:989px;width:18px;height:18px;border-radius:50%;background:#3c8fd0"></div>
<div class="abs partner" style="left:622px;top:993px">Nexaria</div>
<div class="abs partner" style="left:590px;top:1037px;font-size:11px;color:#666">VANTPAG</div>
<div class="abs" style="left:680px;top:1034px;width:19px;height:19px;border-radius:50%;background:#f1b81e"></div>

<div class="abs f-rule"></div>
<div class="abs legal">
  <strong>Pagora</strong> | <strong>Copyright © 2007-2009. Todos os direitos reservados.</strong><br>
  Pagora é um serviço da Pagora Pagamentos S.A., empresa prestadora de serviços de gestão de pagamentos na internet, que atua como agente por conta e ordem dos usuários. O serviço não é, e nem se destina, a ser comparável a serviços financeiros.O uso deste site implica na aceitação dos nossos
</div>
</body>
</html>
```